The Ridgeline Tenets Book Cover

"The Ridgeline Tenets" is a book I wrote with the slogan "Unlock Performance, Spark Engagement: Master the Art of Building Winning Cultures in Today's Hybrid World". The book is designed around a methodology that's mine and that I attached. I would love to see the graphic of the methodology integrated in the design in a very subtle way. Use colors from the model but the book cover should be catchy, modern and engaging to the eye.
Overall the book is about three key elements towards success:
- (Self) Directions (purpose)
- Human experience (people and psychological safety)
- Maximize engagement
The methodology is a FLOW so flow is something that could be incorporated as well in the concept.
Updates
Low design quality
Target Market(s)
Managers and Teams
Look and feel

```html
<!DOCTYPE html>
<html lang="en">
<head>
<meta charset="UTF-8">
<title>The Ridgeline Tenets — Book Cover</title>
<link href="https://fonts.googleapis.com/css2?family=Montserrat:wght@400;800&family=Allura&family=Source+Sans+3:wght@300;400&display=swap" rel="stylesheet">
<style>
  :root {
    --paper: #ffffff;
    --ink: #111111;
    --title-grey: #c3c3c5;
    --sub-grey: #a9a9ab;
    --sky: #5bc2f2;
    --flow-light: rgba(191, 230, 251, 0);
    --flow-mid: rgba(120, 200, 245, 0.55);
    --flow-deep: rgba(63, 134, 216, 0.6);
  }
  html, body {
    margin: 0;
    padding: 0;
    overflow: hidden;
    background: var(--paper);
  }
  .cover {
    position: relative;
    width: 840px;
    height: 1200px;
    background: var(--paper);
    overflow: hidden;
  }
  .author {
    position: absolute;
    top: 66px;
    left: 0;
    width: 100%;
    text-align: center;
    font-family: "Montserrat", sans-serif;
    font-weight: 400;
    font-size: 32px;
    letter-spacing: 10px;
    color: var(--ink);
    margin: 0;
  }
  .title {
    margin: 0;
    font-weight: normal;
  }
  .title-the {
    position: absolute;
    top: 344px;
    left: 0;
    width: 100%;
    text-align: center;
    font-family: "Montserrat", sans-serif;
    font-weight: 400;
    font-size: 52px;
    letter-spacing: 4px;
    color: var(--ink);
    z-index: 3;
  }
  .title-script {
    position: absolute;
    top: 360px;
    left: 0;
    width: 100%;
    text-align: center;
    font-family: "Allura", cursive;
    font-size: 118px;
    color: var(--sky);
    z-index: 3;
  }
  .title-main {
    position: absolute;
    top: 478px;
    left: 0;
    width: 100%;
    text-align: center;
    font-family: "Montserrat", sans-serif;
    font-weight: 800;
    font-size: 146px;
    letter-spacing: -2px;
    color: var(--title-grey);
    z-index: 1;
  }
  .flow-art {
    position: absolute;
    top: 500px;
    left: 0;
    width: 840px;
    height: 360px;
    z-index: 2;
    background: linear-gradient(180deg,
      var(--flow-light) 0%,
      var(--flow-mid) 40%,
      var(--flow-deep) 72%,
      var(--flow-light) 100%);
  }
  .tagline {
    position: absolute;
    top: 904px;
    left: 0;
    width: 100%;
    text-align: center;
    font-family: "Source Sans 3", sans-serif;
    margin: 0;
  }
  .tagline-lead {
    display: block;
    font-weight: 300;
    font-size: 28px;
    color: var(--sub-grey);
    line-height: 30px;
  }
  .tagline-rest {
    display: block;
    font-weight: 300;
    font-size: 27px;
    color: var(--sky);
    line-height: 30px;
  }
</style>
</head>
<body>
<div class="cover">
  <p class="author">AUTHOR NAME</p>

  <h1 class="title">
    <span class="title-the">THE</span>
    <span class="title-script">Ridgeline</span>
    <span class="title-main">TENETS</span>
  </h1>

  <div class="flow-art" role="img" aria-label="Flowing translucent blue wave ribbons sweeping across the cover"></div>

  <p class="tagline">
    <span class="tagline-lead">UNLOCK PERFORMANCE, SPARK ENGAGEMENT:</span>
    <span class="tagline-rest">Master the Art of Building Winning Cultures in Today's Hybrid World</span>
  </p>
</div>
</body>
</html>
```